Mobile and Web design for Remote Skin Condition Service

A new web service that allows patients to upload photos for doctors to review. I need the designs for both mobile (NOT native app) and desktop versions. Key pages are provided in the mockups, and all major form elements are required.
Overall branding and design needed.

We are building an online system that allows patients to connect with a skin doctors.

Users will access the website (typically, but not exclusively via a mobile phone), register, upload photos, answer a few questions and pay to submit their details to a doctor.

The doctor will access the website via a desktop browser and review the case.

The patient’s user flow should be optimised for mobile. It should be usable on desktop too.

The doctor’s user flow should be optimised for desktop. It should be usable on mobile too.

Currently there are no branding restrictions, and no logo, so please be creative.

The site has to look professional, clean and easy to use.
There will be limited text on the pages.
Buttons should be prominent - but they should also obviously be buttons.

Attached are a selection of screens showing most of the functionality of the process - it is not all of the screens of the process but should give the developers enough range and examples.

Target Market(s)

Any user with a skin condition

Industry/Entity Type

Healthcare

Number of Pages Required

5+ page

Colors

Designer to choose colors to be used in the design.

Requirements
Must have
• Mobile and desktop versions of the key pages as per the brief.
• Should be obvious to use - eg the photo upload and camera functions should be standard

```html
<!DOCTYPE html>
<html lang="en">
<head>
<meta charset="utf-8">
<title>Dermaly – Mobile Screens</title>
<link rel="stylesheet" href="https://fonts.googleapis.com/css2?family=Nunito+Sans:wght@300;400;600;700;800&family=Open+Sans:wght@400;600;700&display=swap">
<style>
:root{
  --teal:#6fbaba;
  --brand:#4fb0b3;
  --teal-dark:#0f5562;
  --accent:#3fc9d2;
  --navy:#1e3140;
  --ink:#3c525d;
  --muted:#6f7e88;
  --line:#e8eef0;
  --soft:#eafafc;
  --field:#eef6f7;
  --link:#1a7bd6;
  --bg:#ffffff;
}
*{box-sizing:border-box;margin:0;padding:0}
html,body{width:1200px;height:798px;overflow:hidden;background:var(--bg)}
body{font-family:"Open Sans",sans-serif;color:var(--muted)}
.stage{position:absolute;left:0;top:0;width:2380px;height:1583px;transform:scale(0.50420);transform-origin:0 0}
.screen{position:absolute;width:350px;background:#fff;box-shadow:0 6px 30px rgba(40,70,80,.10);overflow:hidden}
.abs{position:absolute}
/* header */
.topbar{position:absolute;left:0;top:0;width:350px;height:50px;background:#fff;box-shadow:0 2px 8px rgba(0,0,0,.04);z-index:2}
.brand{position:absolute;left:15px;top:16px;font-family:"Nunito Sans",sans-serif;font-weight:800;font-size:15px;letter-spacing:2.2px;color:var(--brand)}
.btn-login{position:absolute;left:231px;top:12px;width:66px;height:26px;border-radius:3px;background:var(--teal);color:#fff;font-size:11px;font-weight:600;display:flex;align-items:center;justify-content:center}
.menu{position:absolute;left:305px;top:12px;width:30px;height:26px;border:1px solid var(--teal);border-radius:4px;display:flex;align-items:center;justify-content:center}
/* type */
.h2{position:absolute;left:16px;font-family:"Nunito Sans",sans-serif;font-weight:300;font-size:23px;color:var(--ink)}
.para{position:absolute;left:16px;width:322px;font-size:12.5px;line-height:20.5px;color:var(--muted)}
.btn{position:absolute;left:16px;width:319px;height:46px;border-radius:3px;color:#fff;font-weight:700;font-size:14px;display:flex;align-items:center;justify-content:center;box-shadow:0 2px 6px rgba(0,0,0,.08)}
.btn-teal{background:var(--teal)}
.btn-navy{background:var(--navy)}
.card{position:absolute;left:16px;width:319px;background:#fff;border:1px solid #f0f4f5;border-radius:4px;box-shadow:0 2px 10px rgba(40,70,80,.05)}
/* hero */
.hero{position:absolute;left:0;top:50px;width:350px;height:198px;background:linear-gradient(90deg,#e4fbfd,#d9f6f9)}
.hero-photo{position:absolute;right:0;top:0;width:160px;height:198px;background:linear-gradient(180deg,#e8d9cf,#cfb6a5 55%,#eef3f4)}
.hero-title{position:absolute;left:16px;top:20px;font-family:"Nunito Sans",sans-serif;color:var(--teal-dark);line-height:42px}
.hero-title .l1{font-weight:300;font-size:32px;display:block}
.hero-title .l2{font-weight:700;font-size:34px;display:block}
.dots{position:absolute;display:flex;gap:7px}
.dots i{width:7px;height:7px;border-radius:50%;background:#dfe7ea;display:block}
.dots i.on{background:var(--accent)}
.feature{height:94px;display:flex;align-items:center;padding-left:10px}
.feature .ic{width:64px;height:64px;border-radius:50%;background:var(--soft);display:flex;align-items:center;justify-content:center;flex:none}
.feature p{margin-left:24px;font-size:13px;font-weight:600;line-height:21px;color:var(--teal-dark)}
.rule{position:absolute;left:16px;width:319px;height:1px;background:var(--line)}
.avatar{position:absolute;left:145px;width:60px;height:60px;border-radius:50%;background:linear-gradient(160deg,#c9b3a3,#7d6a60);border:3px solid #eef6f7}
.legal{position:absolute;left:0;width:350px;text-align:center;font-size:9px;font-weight:700;color:var(--navy);line-height:14px}
.legal a{color:var(--link);text-decoration:underline}
/* steps */
.illus{position:absolute;left:0;top:50px;width:350px;height:207px;background:linear-gradient(180deg,#f6f8f9,#eef5f7)}
.step{position:absolute;left:18px;display:flex;align-items:center;font-size:13px;color:#3d4f59}
.step b{width:26px;height:26px;border-radius:50%;background:var(--teal);color:#fff;font-size:11px;display:flex;align-items:center;justify-content:center;border:3px solid #d6eeee;margin-right:14px}
/* form */
.step-no{position:absolute;left:16px;top:68px;width:33px;height:33px;border-radius:50%;border:1.5px solid #7c8b93;font-family:"Nunito Sans",sans-serif;font-size:18px;color:var(--ink);display:flex;align-items:center;justify-content:center}
.step-title{position:absolute;left:61px;top:67px;font-family:"Nunito Sans",sans-serif;font-weight:400;font-size:23px;color:var(--ink)}
.label{position:absolute;left:17px;font-size:9px;color:var(--muted)}
.field{position:absolute;left:16px;width:319px;height:47px;border:1px solid #edf2f4;border-radius:3px;background:#fff;box-shadow:0 1px 4px rgba(0,0,0,.03);font-size:12px;display:flex;align-items:center;padding-left:14px;color:#27343b}
.field .ph{color:#bcc6cb;font-size:11px}
.seg{position:absolute;left:16px;width:319px;height:47px;display:flex;border:1px solid #edf2f4;border-radius:3px;overflow:hidden}
.seg span{flex:1;display:flex;align-items:center;justify-content:center;font-size:13px;color:var(--muted)}
.seg span.on{background:var(--field)}
.note{position:absolute;left:17px;font-size:9px;font-weight:700;color:var(--navy)}
.q{position:absolute;left:16px;width:325px;font-size:11.5px;line-height:20px;color:#55646d}
.select{position:absolute;left:16px;top:170px;width:52px;height:25px;border:1px solid #edf2f4;border-radius:3px;font-size:11px;color:#27343b;display:flex;align-items:center;padding-left:9px;gap:14px}
.units{position:absolute;left:85px;top:170px;width:160px;height:25px;display:flex;border:1px solid #edf2f4;border-radius:3px;overflow:hidden}
.units span{flex:1;display:flex;align-items:center;justify-content:center;font-size:9px;color:var(--muted)}
.units span.on{background:var(--accent);color:#fff}
.textarea{position:absolute;left:16px;top:268px;width:319px;height:142px;border:1px solid #edf2f4;border-radius:3px;padding:13px 14px;font-size:11px;color:#bcc6cb}
.radios{position:absolute;left:20px;display:flex;align-items:center;font-size:8.5px;color:var(--muted)}
.radio{width:15px;height:15px;border-radius:50%;border:1px solid #d5e8ea;display:flex;align-items:center;justify-content:center;margin-right:7px}
.radio.on::after{content:"";width:9px;height:9px;border-radius:50%;background:var(--accent)}
</style>
</head>
<body>
<div class="stage">

  <!-- Screen: landing -->
  <section class="screen" style="left:185px;top:150px;height:1228px">
    <header class="topbar">
      <div class="brand">DERMALY</div>
      <div class="btn-login">Login</div>
      <div class="menu"><svg width="16" height="12" viewBox="0 0 16 12"><path d="M0 1h16M0 6h16M0 11h16" stroke="#6fbaba" stroke-width="1.4"/></svg></div>
    </header>
    <div class="hero">
      <div class="hero-photo" role="img" aria-label="Photo of a smiling doctor with a stethoscope"></div>
      <h1 class="hero-title"><span class="l1">Choice Of</span><span class="l2">Happiness</span></h1>
      <div class="dots" style="left:143px;top:184px"><i></i><i></i><i class="on"></i><i></i><i></i></div>
    </div>
    <h2 class="h2" style="top:275px">We Care About Your Health</h2>
    <p class="para" style="top:318px">Contrary to popular belief, Lorem Ipsum is not simply random text. It has roots in a piece of classical Latin literature from 45 BC making it over 2000 years old.</p>

    <div class="card feature" style="top:407px">
      <div class="ic"><svg width="42" height="42" viewBox="0 0 42 42" fill="none" stroke="#3fc9d2" stroke-width="2"><circle cx="21" cy="21" r="18"/><circle cx="21" cy="21" r="12"/><path d="M21 21l5-6"/><circle cx="21" cy="21" r="1.6" fill="#3fc9d2"/></svg></div>
      <p>The waiting is finally over! no<br>waiting in long queues at clinics</p>
    </div>
    <div class="card feature" style="top:512px">
      <div class="ic"><svg width="42" height="38" viewBox="0 0 42 38" fill="none" stroke="#3fc9d2" stroke-width="2"><rect x="2" y="10" width="26" height="18" rx="2"/><path d="M8 28v6l6-6"/><path d="M14 10V4h26v18h-12"/><path d="M7 16h16M7 21h12"/></svg></div>
      <p>Traffic is not a problem anymore,<br>consult a doctor from home</p>
    </div>
    <div class="card feature" style="top:617px">
      <div class="ic"><svg width="42" height="38" viewBox="0 0 42 38" fill="none" stroke="#3fc9d2" stroke-width="2"><rect x="3" y="12" width="36" height="22" rx="2"/><path d="M8 12l12-9 13 9"/><path d="M25 23h8"/><circle cx="13" cy="23" r="3"/></svg></div>
      <p>Simple, convenient &amp; affordable</p>
    </div>

    <div class="rule" style="top:745px"></div>
    <h2 class="h2" style="top:767px;left:0;width:350px;text-align:center">Connected to Serve Better</h2>
    <div class="card" style="top:818px;height:250px"></div>
    <div class="avatar" style="top:842px" role="img" aria-label="Portrait photo of the patient"></div>
    <div class="abs" style="left:0;top:917px;width:350px;text-align:center;font-size:13px;font-weight:600;color:#3d4f59">Mira Holloway</div>
    <p class="abs" style="left:35px;top:945px;width:290px;font-size:12.5px;line-height:24.5px;color:var(--muted)">Lorem Ipsum is simply dummy text of the printing and typesetting industry. Lorem Ips has been the inry's standard dummy text ever since</p>
    <div class="dots" style="left:157px;top:1044px"><i></i><i class="on"></i><i></i></div>

    <div class="btn btn-teal" style="top:1093px">Get Diagnosed</div>
    <div class="rule" style="top:1160px"></div>
    <div class="legal" style="top:1178px">© 2020 Dermaly. All rights reserved.</div>
    <div class="legal" style="top:1199px"><a>Privacy Police</a> &nbsp;-&nbsp; <a>Terms of Service</a></div>
  </section>

  <!-- Screen: how it works -->
  <section class="screen" style="left:733px;top:150px;height:770px">
    <header class="topbar">
      <div class="brand">DERMALY</div>
      <div class="btn-login">Login</div>
      <div class="menu"><svg width="16" height="12" viewBox="0 0 16 12"><path d="M0 1h16M0 6h16M0 11h16" stroke="#6fbaba" stroke-width="1.4"/></svg></div>
    </header>
    <div class="illus" role="img" aria-label="Illustration of a patient consulting a doctor online from home"></div>
    <h2 class="h2" style="top:275px">A Short Catchy Headline</h2>
    <p class="para" style="top:318px">Contrary to popular belief, Lorem Ipsum is not simply random text. It has roots in a piece of classical Latin literature from 45 BC making it over 2000 years old.</p>
    <div class="card" style="top:400px;height:228px"></div>
    <div class="step" style="top:418px"><b>1</b>Take or upload 3 photos</div>
    <div class="step" style="top:460px"><b>2</b>Tell us a little about yourself</div>
    <div class="step" style="top:501px"><b>3</b>Answer a few medical questions</div>
    <div class="step" style="top:543px"><b>4</b>Make a secure online payment</div>
    <div class="step" style="top:584px"><b>5</b>Wait just 24hours for your diagnosis</div>
    <div class="btn btn-navy" style="top:653px">Ready to Start?</div>
    <div class="legal" style="top:711px">*By selecting "Ready to Start?", you agree to our <a>Terms of Service</a><br>(including the mandatory arbitration of disputes) and consent to our<br><a>Privacy Policy.</a></div>
  </section>

  <!-- Screen: about you -->
  <section class="screen" style="left:1281px;top:150px;height:700px">
    <header class="topbar">
      <div class="brand">DERMALY</div>
      <div class="btn-login">Login</div>
      <div class="menu"><svg width="16" height="12" viewBox="0 0 16 12"><path d="M0 1h16M0 6h16M0 11h16" stroke="#6fbaba" stroke-width="1.4"/></svg></div>
    </header>
    <div class="step-no">2</div>
    <h2 class="step-title">Tell us about yourself</h2>
    <div class="rule" style="top:118px"></div>
    <p class="q" style="top:138px;width:320px">Thank you for the photographs. We now need a little bit more information about you.</p>
    <div class="label" style="top:203px">Your name</div>
    <div class="field" style="top:223px"></div>
    <div class="label" style="top:281px">Gender</div>
    <div class="seg" style="top:301px"><span class="on">Male</span><span>Female</span></div>
    <div class="label" style="top:359px">Date of birth</div>
    <div class="field" style="top:379px;justify-content:space-between;padding-right:12px"><span class="ph">DD-MM-YYYY</span>
      <svg width="14" height="14" viewBox="0 0 14 14" fill="none" stroke="#b5c0c5" stroke-width="1.2"><rect x="1" y="2.5" width="12" height="10.5" rx="1"/><path d="M1 5.5h12M4 1v3M10 1v3"/><rect x="8" y="8" width="2.5" height="2.5" fill="#b5c0c5" stroke="none"/></svg></div>
    <div class="label" style="top:440px">Email address</div>
    <div class="field" style="top:457px">Sam Rowe<span style="width:1px;height:14px;background:#27343b;margin-left:1px"></span></div>
    <div class="label" style="top:517px">Confirm email address</div>
    <div class="field" style="top:535px"></div>
    <div class="note" style="top:594px">*We'll send you and email to set a password for the account</div>
    <div class="btn btn-teal" style="top:630px">Next Step</div>
  </section>

  <!-- Screen: condition questions -->
  <section class="screen" style="left:1829px;top:150px;height:722px">
    <header class="topbar">
      <div class="brand">DERMALY</div>
      <div class="btn-login">Login</div>
      <div class="menu"><svg width="16" height="12" viewBox="0 0 16 12"><path d="M0 1h16M0 6h16M0 11h16" stroke="#6fbaba" stroke-width="1.4"/></svg></div>
    </header>
    <div class="step-no">3</div>
    <h2 class="step-title">Question about condition</h2>
    <div class="rule" style="top:118px"></div>
    <p class="q" style="top:138px">How long have you had this condition?</p>
    <div class="select">0 <svg width="10" height="6" viewBox="0 0 10 6"><path d="M1 1l4 4 4-4" stroke="#55646d" fill="none" stroke-width="1.3"/></svg></div>
    <div class="units"><span class="on">Days</span><span>Months</span><span>Years</span></div>
    <p class="q" style="top:219px">Have you tried medication previously? If so, please list it Give as much detail as possible about the medicine.</p>
    <div class="textarea">Your message here...</div>

    <p class="q" style="top:434px;left:20px">If so, please list it Give as much detail as possible</p>
    <div class="radios" style="top:463px"><span class="radio on"></span>Yes<span class="radio" style="margin-left:34px"></span>No</div>
    <p class="q" style="top:509px;left:20px">If so, please list it Give as much detail as possible</p>
    <div class="radios" style="top:538px"><span class="radio on"></span>Yes<span class="radio" style="margin-left:34px"></span>No</div>
    <p class="q" style="top:583px;left:20px">If so, please list it Give as much detail as possible</p>
    <div class="radios" style="top:612px"><span class="radio on"></span>Yes<span class="radio" style="margin-left:34px"></span>No</div>

    <div class="btn btn-teal" style="top:653px">Next Step</div>
  </section>

</div>
</body>
</html>
```